Corporate Branding - Web and Print

A UK based company will like to use an existing logo to create branding materials for all marketing related documents, including business card, prints, letterhead, Website, Twitter, Facebook, Instagram logo etc. This company serves high-end clientele in the fashion, health and wellness and as such high quality and class is of utmost importance.
Where the logo can be modernised without losing its character then experiment. The main thing is to have a corporate branding which can be used later for brochures, Business Plan infographics.
The prominent colour within the organisation is burnt orange with no secondary colour. However if you believe a secondary colour is needed then use it, otherwise keep it simple and classy. Any chosen colours have to match perfectly.
Target Market(s)
High net worth individuals
Industry/Entity Type
Health And Wellness
Contact Information for Business Card
classy
Look and feel
Each slider illustrates characteristics of the customer's brand and the style your logo design should communicate.

```html
<!DOCTYPE html>
<html lang="en">
<head>
<meta charset="UTF-8">
<title>Velora Business Card</title>
<link href="https://fonts.googleapis.com/css2?family=Open+Sans:wght@400;600;700&family=Montserrat:wght@800&display=swap" rel="stylesheet">
<style>
  :root {
    --burnt-orange: #f7931e;
    --card-black: #1a1818;
    --text-white: #f4f4f4;
    --stage: #eef0f2;
    --photo-pink: #d1467f;
    --photo-teal: #3fa9b5;
    --photo-blue: #6f93c8;
    --photo-grey: #b9b2b4;
  }
  * { margin: 0; padding: 0; box-sizing: border-box; }
  html, body { width: 1200px; height: 936px; overflow: hidden; }
  body {
    background: var(--stage);
    font-family: "Open Sans", sans-serif;
    display: flex;
    flex-direction: column;
    align-items: center;
    justify-content: center;
    gap: 60px;
  }
  .card {
    width: 630px;
    height: 360px;
    position: relative;
    overflow: hidden;
    box-shadow: 0 10px 30px rgba(0,0,0,0.18);
  }
  .brand-name {
    font-family: "Montserrat", sans-serif;
    font-weight: 800;
    color: var(--burnt-orange);
    letter-spacing: 2px;
    display: flex;
    align-items: center;
    gap: 12px;
    white-space: nowrap;
  }
  .brand-dot {
    border-radius: 50%;
    background: var(--burnt-orange);
    flex-shrink: 0;
  }

  /* Front */
  .card-front .photo-fill {
    position: absolute; inset: 0;
    background:
      radial-gradient(ellipse at 65% 35%, var(--photo-pink) 0%, transparent 38%),
      radial-gradient(ellipse at 45% 65%, var(--photo-teal) 0%, transparent 35%),
      radial-gradient(ellipse at 12% 40%, var(--photo-blue) 0%, transparent 40%),
      linear-gradient(135deg, var(--photo-grey), #8a8184 55%, #2b2728);
  }
  .card-front .brand-name {
    position: absolute;
    left: 60px; top: 50%;
    transform: translateY(-50%);
    font-size: 60px;
  }
  .card-front .brand-dot { width: 50px; height: 50px; }

  /* Back */
  .card-back {
    background: var(--card-black);
    display: flex;
    align-items: center;
    justify-content: space-between;
    padding: 0 44px 0 48px;
    gap: 30px;
  }
  .card-back .brand-name { font-size: 34px; align-self: flex-end; margin-bottom: 110px; }
  .card-back .brand-dot { width: 28px; height: 28px; }
  .details { width: 260px; flex-shrink: 0; }
  .person-name {
    color: var(--burnt-orange);
    font-weight: 700;
    font-size: 23px;
    line-height: 1.15;
  }
  .person-role {
    color: var(--text-white);
    font-size: 16px;
    margin-bottom: 18px;
  }
  .contact-list { list-style: none; }
  .contact-list li {
    display: flex;
    align-items: flex-start;
    gap: 12px;
    color: var(--text-white);
    font-size: 12.5px;
    line-height: 1.35;
    margin-bottom: 4px;
  }
  .contact-list svg {
    width: 14px; height: 14px;
    flex-shrink: 0;
    margin-top: 2px;
    fill: var(--burnt-orange);
  }
</style>
</head>
<body>

<section class="card card-front">
  <div class="photo-fill" role="img" aria-label="Photograph of women stretching in a bright fitness class"></div>
  <div class="brand-name"><span class="brand-dot"></span>VELORA</div>
</section>

<section class="card card-back">
  <div class="brand-name"><span class="brand-dot"></span>VELORA</div>
  <div class="details">
    <p class="person-name">Corwin Ashdale</p>
    <p class="person-role">Personal Trainer</p>
    <ul class="contact-list">
      <li>
        <svg viewBox="0 0 16 16"><path d="M8 1a5 5 0 0 0-5 5c0 4 5 9 5 9s5-5 5-9a5 5 0 0 0-5-5zm0 7a2 2 0 1 1 0-4 2 2 0 0 1 0 4z"/></svg>
        <span>Suite 103, Street 01, Zip Code<br>City Country</span>
      </li>
      <li>
        <svg viewBox="0 0 16 16"><path d="M4 1l2.5 3-1.5 2c1 2 2.5 3.5 5 5l2-1.5 3 2.5-1.5 2.5C7 14 2 9 1.5 2.5z"/></svg>
        <span>123 555 0147</span>
      </li>
      <li>
        <svg viewBox="0 0 16 16"><path d="M1 3h14v10H1zm1.5 1.2L8 8.5l5.5-4.3z"/></svg>
        <span>info@velora.com</span>
      </li>
      <li>
        <svg viewBox="0 0 16 16"><path d="M8 1a7 7 0 1 0 0 14A7 7 0 0 0 8 1zm0 1.5c.8 0 1.8 1.8 2 4.5H6c.2-2.7 1.2-4.5 2-4.5zM2.6 9h2.9c.1 1.6.5 3 1 3.9A5.5 5.5 0 0 1 2.6 9zm0-2a5.5 5.5 0 0 1 3.9-3.9c-.5.9-.9 2.3-1 3.9zm3.4 2h4c-.2 2.7-1.2 4.5-2 4.5s-1.8-1.8-2-4.5zm3.5 3.9c.5-.9.9-2.3 1-3.9h2.9a5.5 5.5 0 0 1-3.9 3.9zM10.5 7c-.1-1.6-.5-3-1-3.9A5.5 5.5 0 0 1 13.4 7z"/></svg>
        <span>www.velora.com</span>
      </li>
      <li>
        <svg viewBox="0 0 16 16"><circle cx="8" cy="8" r="5.5"/></svg>
        <span>@veloraApp</span>
      </li>
      <li>
        <svg viewBox="0 0 16 16"><circle cx="8" cy="8" r="5.5"/></svg>
        <span>@JoinVelora</span>
      </li>
      <li>
        <svg viewBox="0 0 16 16"><circle cx="8" cy="8" r="5.5"/></svg>
        <span>@veloraApp</span>
      </li>
    </ul>
  </div>
</section>

</body>
</html>
```